Client questionnaire

Quillon Ravenmoor Group (www.quillonravenmoor.com.au) needs a document designed to bring out as a questionnaire to speak with potential clients. Sales staff and planners will use this in introductions to ask basic questions but to also scribble notes and draw pictures on top of the graph.
I've attached two files which are the content that we wish to include.
1. Financial life cycle: this has two pages. Please design it so that the financial snap shot is on a different page than the lifecycle and graph. I will leave it to the designer to decide whether landscape or portrait is best - please ensure though that they are both landscape or both portrait on this document as they will be printed back to back on the same sheet.
2. Goals diagram - please theme this in the same way as the above document.
3. I've attached the logo to be used too - filename: QuillonRavenmoorgroup.eps

Group

```html
<!DOCTYPE html>
<html lang="en">
<head>
<meta charset="utf-8">
<title>Your Financial Snapshot</title>
<link rel="stylesheet" href="https://fonts.googleapis.com/css2?family=Montserrat:wght@300;400&display=swap">
<style>
  :root {
    --paper: #ffffff;
    --band: #939393;
    --rule: #6e6e6e;
    --ink: #3a3a3a;
    --band-ink: #ffffff;
  }
  * { box-sizing: border-box; margin: 0; padding: 0; }
  html, body { width: 849px; height: 1200px; overflow: hidden; background: var(--paper); }
  body { font-family: "Montserrat", Arial, sans-serif; font-weight: 300; color: var(--ink); }
  .sheet { position: relative; width: 849px; height: 1200px; }

  .section-band {
    position: absolute; left: 40px; width: 768px; height: 44px;
    background: var(--band); color: var(--band-ink);
    font-size: 19px; letter-spacing: 0.4px; line-height: 44px;
  }
  .section-band.left { padding-left: 29px; }
  .section-band.centred { text-align: center; }

  .form-table {
    position: absolute; left: 40px; width: 768px;
    border-collapse: collapse; table-layout: fixed;
    font-size: 16px; letter-spacing: 0.2px;
  }
  .form-table td, .form-table th {
    border: 1px solid var(--rule); height: 24.7px; padding: 0 0 0 28px;
    font-weight: 300; text-align: left; white-space: nowrap; vertical-align: middle;
  }
  .form-table .value-cell { padding-left: 10px; }
  .form-table .head th { background: var(--band); color: var(--band-ink); border-color: var(--band); }
  .form-table .head th.mid { text-align: center; padding: 0; }
  .form-table .label-band { background: var(--band); color: var(--band-ink); }
  .form-table .shaded { background: var(--band); }

  .personal { top: 88px; }
  .assets { top: 316px; }
  .liabilities { top: 567px; }

  .consent {
    position: absolute; left: 40px; top: 770px; width: 772px;
    font-size: 15.3px; line-height: 17.2px; letter-spacing: 0.05px;
  }
  .sign-line {
    position: absolute; left: 40px; font-size: 15.5px;
  }
  .sign-line .blank { display: inline-block; border-bottom: 1px solid var(--ink); height: 14px; vertical-align: baseline; }
  .signature { top: 1095px; }
  .date { top: 1129px; }
</style>
</head>
<body>
<main class="sheet">

  <div class="section-band left" style="top:40px">YOUR FINANCIAL SNAPSHOT...</div>
  <table class="form-table personal">
    <colgroup><col style="width:183px"><col style="width:202px"><col style="width:182px"><col style="width:201px"></colgroup>
    <tr><td class="label-band">Your’s details</td><td></td><td class="label-band">Partner's details</td><td></td></tr>
    <tr><td>Name:</td><td></td><td>Name:</td><td></td></tr>
    <tr><td>D.O.B:</td><td></td><td>D.O.B:</td><td></td></tr>
    <tr><td>Occupation:</td><td></td><td>Occupation:</td><td></td></tr>
    <tr><td>Annual salary:</td><td class="value-cell">$</td><td>Annual salary:</td><td class="value-cell">$</td></tr>
    <tr><td>Children:</td><td></td><td>Child’s age:</td><td></td></tr>
  </table>

  <div class="section-band centred" style="top:267px">ASSETS</div>
  <table class="form-table assets">
    <colgroup><col style="width:212px"><col style="width:173px"><col style="width:182px"><col style="width:201px"></colgroup>
    <tr class="head"><th>Description</th><th class="mid">Date purchased</th><th class="mid">Value</th><th class="mid">Details</th></tr>
    <tr><td>Residential home</td><td></td><td class="value-cell">$</td><td></td></tr>
    <tr><td>Investment property</td><td></td><td class="value-cell">$</td><td></td></tr>
    <tr><td>Cash</td><td></td><td class="value-cell">$</td><td></td></tr>
    <tr><td>Car(s)</td><td></td><td class="value-cell">$</td><td></td></tr>
    <tr><td>Superannuation</td><td></td><td class="value-cell">$</td><td></td></tr>
    <tr><td>Total Assets</td><td class="shaded"></td><td class="value-cell">$</td><td></td></tr>
  </table>

  <div class="section-band centred" style="top:519px">LIABILITIES</div>
  <table class="form-table liabilities">
    <colgroup><col style="width:212px"><col style="width:86px"><col style="width:87px"><col style="width:182px"><col style="width:201px"></colgroup>
    <tr class="head"><th>Description</th><th class="mid">Lender</th><th class="mid">Term</th><th class="mid">Amount</th><th class="mid">Details</th></tr>
    <tr><td>Residential home</td><td></td><td></td><td class="value-cell">$</td><td></td></tr>
    <tr><td>Investment property</td><td></td><td></td><td class="value-cell">$</td><td></td></tr>
    <tr><td>Personal loan</td><td></td><td></td><td class="value-cell">$</td><td></td></tr>
    <tr><td>Car loan</td><td></td><td></td><td class="value-cell">$</td><td></td></tr>
    <tr><td>Credit cards</td><td></td><td></td><td class="value-cell">$</td><td></td></tr>
    <tr><td>Total Liabilities</td><td class="shaded" colspan="2"></td><td class="value-cell">$</td><td></td></tr>
  </table>

  <p class="consent">I/We consent to you using personal and credit information about me/us for the purpose of arranging or providing credit, insuring credit, and for direct marketing of products and services offered by you or any organisation you are affiliated with or represent.<br>The personal information provided by me/us will be held by you. I/We can gain access to the information by contacting you. I/We have the right to request not to receive marketing material. You may disclose personal information about me/us as required by law, or to organisations involved in providing credit to me/us, any of your associates or contractors, (including, for example, stationary printing houses, mail houses, lawyers, accountants), or people considering acquiring or taking an interest in your business or assets. I/We hereby authorise you to receive information from any lender about our credit affairs, and to provide any relevant real estate agent, lawyer, or conveyance with details of whether finance has been approved for us, and if it has the terms of that approval, including providing a copy of any approval letter. I/we may disclose personal information to any industry body, tribunal, court or otherwise in connection with any complain regarding the approval or management of your loan - for example if a complaint is lodged about me/us or the lender.</p>

  <div class="sign-line signature">Signature(s): <span class="blank" style="width:276px"></span></div>
  <div class="sign-line date">Date: <span class="blank" style="width:28px"></span> /<span class="blank" style="width:28px"></span> /<span class="blank" style="width:28px"></span></div>

</main>
</body>
</html>
```